Book cover for ebook and Physical book for Mind Clutter Collective

I run a non-profit Mind Clutter Collective and I have a new book that needs a cover. For the physical book, I will need a full wrap. The mission is to help individuals Quiet the cycle of restless worry patterns. This book is title is "Quiet the cycle of restless worry patterns", and subtitle "Clear Your Mind of Static Noise." I am open to anything design wise, nothing is set in stone. Oh, MCC is pending Trademark.

Target Market(s)

Typically it's Mom's from 25-40

Industry/Entity Type

Mental Health

Font styles to use
Serif

Colors
f37122
9bcb3b
fbed22
0255a3
e34197

Requirements
Must have
• I do like simplicity, yet vibrant colors.
Nice to have
• The authors are Rex T. Whitford, and Dana Okonkwo. For some inspiration individuals refer to me as the Wonder Guide having reversed five incurable diseases.
Should not have
• The cover shouldn't be too busy.

```html
<!DOCTYPE html>
<html lang="en">
<head>
<meta charset="utf-8">
<title>Quiet the Cycle of Restless Worry Patterns — Book Cover</title>
<link rel="stylesheet" href="https://fonts.googleapis.com/css2?family=Bebas+Neue&family=Roboto+Serif:wdth,wght@50..150,100..900&display=swap">
<style>
  :root {
    --slate-dark: #2e2e2e;
    --slate-mid: #474747;
    --title-white: #ffffff;
    --subtitle-gold: #f7c300;
    --sky-top: #2f7fd0;
    --sky-low: #a9cdea;
    --field-yellow: #f3dd1c;
    --field-green: #5fb82a;
    --grass-deep: #3e9a1e;
    --band: rgba(40, 40, 40, 0.78);
  }
  html, body {
    margin: 0;
    padding: 0;
    width: 800px;
    height: 1200px;
    overflow: hidden;
    background: #ffffff;
  }
  .cover {
    position: relative;
    width: 800px;
    height: 1200px;
    overflow: hidden;
    background: radial-gradient(ellipse at 50% 35%, var(--slate-mid) 0%, var(--slate-dark) 85%);
    font-family: "Bebas Neue", "Oswald", sans-serif;
  }
  .title-block {
    position: absolute;
    left: 0;
    top: 0;
    width: 800px;
    height: 800px;
  }
  .title-line {
    fill: var(--title-white);
    font-family: "Bebas Neue", "Oswald", sans-serif;
  }
  .subtitle-line {
    fill: var(--subtitle-gold);
    font-family: "Roboto Serif", "Georgia", serif;
    font-weight: 700;
    font-stretch: 50%;
    font-variation-settings: "wdth" 50;
  }
  .landscape {
    position: absolute;
    left: 0;
    top: 804px;
    width: 800px;
    height: 396px;
    background: linear-gradient(
      to bottom,
      var(--sky-top) 0%,
      var(--sky-low) 24%,
      var(--field-yellow) 28%,
      var(--field-yellow) 42%,
      var(--field-green) 50%,
      var(--grass-deep) 100%
    );
  }
  .author-band {
    position: absolute;
    left: 0;
    top: 1116px;
    width: 800px;
    height: 52px;
    background: var(--band);
    display: flex;
    align-items: center;
    justify-content: center;
  }
  .author-names {
    margin: 0;
    color: var(--title-white);
    font-size: 38px;
    letter-spacing: 1px;
    line-height: 1;
    padding-top: 4px;
  }
</style>
</head>
<body>
  <main class="cover">
    <svg class="title-block" width="800" height="800" viewBox="0 0 800 800" aria-labelledby="book-title">
      <title id="book-title">Quiet the Cycle of Restless Worry Patterns — Clear Your Mind of Static Noise</title>
      <text class="title-line" x="124" y="164" font-size="131" textLength="552" lengthAdjust="spacing">QUIET</text>
      <text class="title-line" x="124" y="260" font-size="77" textLength="552" lengthAdjust="spacing">THE CYCLE OF</text>
      <text class="title-line" x="124" y="388" font-size="137" textLength="552" lengthAdjust="spacing">RESTLESS</text>
      <text class="title-line" x="124" y="528" font-size="154" textLength="552" lengthAdjust="spacing">WORRY</text>
      <text class="title-line" x="124" y="672" font-size="150" textLength="552" lengthAdjust="spacing">PATTERNS</text>
      <text class="subtitle-line" x="124" y="750" font-size="44" textLength="552" lengthAdjust="spacingAndGlyphs">CLEAR YOUR MIND OF STATIC NOISE</text>
    </svg>

    <div class="landscape" role="img" aria-label="Photo of a person with raised arms pushing up the dark sky above a bright yellow flower field, green meadow and distant mountains under a blue sky"></div>

    <div class="author-band">
      <p class="author-names">REX T. WHITFORD &amp; DANA OKONKWO</p>
    </div>
  </main>
</body>
</html>
```